School learning environment project dashboard

We have an online learning enviroment for schools (12 / 18 year). Within this enviroment students work on projects.

Attached we have a setup we have created for a project, but we are looking for more ideas to make this even better, more sexy and still keep it functional for teachers and students.

The attached files show one dashboard we have. This dashboard holds the roadmap for the student, upcoming appointments, latest messages and the main documents the student is working on.

Target Market(s)

schools

Number of Pages Required

1 page

Font styles to use
Sans Serif

```html
<!DOCTYPE html>
<html lang="en">
<head>
<meta charset="utf-8">
<title>Project dashboard</title>
<link rel="stylesheet" href="https://fonts.googleapis.com/css2?family=Catamaran:wght@400;500;600;700&display=swap">
<style>
:root{
  --stage:#e0e0e0;
  --ink:#2b2540;
  --muted:#7b7888;
  --header-dark:#3a2c4a;
  --header-side:#7a6e8c;
  --sidebar:#ebeaee;
  --blue:#2c8fd6;
  --cyan:#1fb7e8;
  --green:#3fd61a;
  --green-soft:#cdf5c3;
  --blue-soft:#c2e2f8;
  --peach-soft:#fde6c3;
  --pink-soft:#fbd1df;
  --yellow:#d6e33a;
  --yellow-dot:#d9d91c;
  --yellow-soft:#f5f7d6;
  --red:#e0175c;
  --card:#ebe9ee;
  --card-line:#c9c6cf;
  --post:#e4d7ee;
  --post-line:#b79fd0;
  --footer:#c3e2f9;
  --popup:#bfe3fb;
  --popup-line:#8ccaf2;
  --white:#ffffff;
}
*{box-sizing:border-box;margin:0;padding:0}
html,body{width:1200px;height:1200px;overflow:hidden;background:var(--stage);font-family:"Catamaran",sans-serif;color:var(--ink)}
.screen{position:absolute;top:357px;width:890px;height:783px;background:var(--white);transform:scale(0.6211);transform-origin:0 0;overflow:hidden;box-shadow:0 6px 14px rgba(0,0,0,.18)}
.screen-a{left:36px}
.screen-b{left:611px}
.abs{position:absolute}
.header{left:0;top:0;width:890px;height:89px;background:linear-gradient(100deg,#2b1f3f 0%,#4a3a55 45%,#6b5a5e 75%,#4b3b45 100%)}
.sidebar{left:36px;top:0;width:188px;height:783px;background:var(--sidebar)}
.sidebar-head{left:36px;top:0;width:188px;height:89px;background:var(--header-side)}
.footer{left:0;top:748px;width:890px;height:35px;background:var(--footer)}
.avatar{left:37px;top:37px;width:52px;height:52px;border-radius:50%;border:3px solid var(--green);background:linear-gradient(160deg,#a48f7c,#5d4c45)}
.welcome{left:96px;top:44px;font-size:15px;font-weight:600;color:var(--green)}
.user-name{left:96px;top:62px;font-size:15px;font-weight:700;color:var(--white)}
.brand{left:250px;top:10px;font-size:20px;font-weight:700;color:var(--white)}
.crumbs{left:250px;top:67px;font-size:9px;color:var(--white)}
.crumbs b{color:var(--cyan);font-weight:500}
.top-dot{top:20px;width:15px;height:15px;border-radius:50%;background:var(--white)}
.top-dot i{position:absolute;top:-3px;right:-3px;width:6px;height:6px;border-radius:50%;background:var(--red)}
.tab{top:110px;font-size:14px;color:var(--muted)}
.tab.active{color:var(--blue);font-weight:700;border-bottom:2px solid var(--blue);padding-bottom:3px}
.tool-icon{top:112px;width:12px;height:12px;border-radius:3px;background:var(--ink)}
.nav{left:80px;font-size:14px;color:var(--muted)}
.nav.strong{color:var(--ink);font-weight:700}
.nav.current{color:var(--ink);border-bottom:1px solid var(--ink)}
.nav-icon{left:54px;width:12px;height:11px;border-radius:3px;background:#5f5a70}
.burger{left:195px;top:151px;width:12px;height:10px;border-top:2px solid var(--ink);border-bottom:2px solid var(--ink)}
.burger::after{content:"";position:absolute;left:0;top:2px;width:12px;height:2px;background:var(--ink)}
.section-title{font-size:14px;font-weight:600;color:#4a4656}
.view-all{font-size:11px;color:var(--muted)}
.arrow-btn{top:169px;width:16px;height:16px;border-radius:50%}
.arrow-btn.prev{left:786px;border:1px solid var(--muted)}
.arrow-btn.next{left:822px;background:var(--ink)}
.timeline{left:250px;top:196px;width:587px;height:70px;border:2px solid var(--yellow);border-radius:5px}
.track{left:290px;top:232px;width:510px;border-top:1px dotted #a9a6b0}
.step{top:215px;width:34px;height:34px;border-radius:50%;text-align:center;line-height:36px;font-size:14px;font-weight:700;color:#3b3550}
.step.done{background:var(--green-soft)}
.step.edit{background:var(--blue-soft)}
.step.wait{background:var(--peach-soft)}
.step.stop{background:var(--pink-soft)}
.badge{position:absolute;top:-9px;right:-4px;width:14px;height:14px;border-radius:4px;display:block}
.badge svg{display:block}
.step-date{top:251px;width:60px;text-align:center;font-size:8px;color:#9c99a6}
.doc{left:250px;width:266px;height:53px;border:1px solid #ecefb8;border-radius:5px;background:var(--white)}
.doc.featured{background:var(--yellow-soft);border-color:#dfe67f}
.doc-label{position:absolute;left:38px;top:17px;font-size:14px;color:var(--muted)}
.doc-icon{position:absolute;top:20px;width:12px;height:12px;border-radius:3px;background:var(--ink)}
.doc-icon.light{background:#9d99a8}
.appt{left:552px;width:267px;height:53px;background:var(--card);border:1px solid var(--card-line);border-radius:5px;box-shadow:0 2px 3px rgba(0,0,0,.12)}
.appt-title{position:absolute;left:17px;top:16px;font-size:13px;color:var(--ink)}
.appt-date{position:absolute;left:17px;top:35px;font-size:8px;color:#9c99a6}
.appt-flag{position:absolute;right:17px;top:20px;width:11px;height:11px;border-radius:3px}
.pill{left:785px;top:377px;width:53px;height:14px;border-radius:7px;background:#dff6d5;border:1px solid #bfe8ad;font-size:7px;text-align:center;line-height:13px;color:#4a4656}
.post-author{left:552px;top:613px;font-size:10px;font-weight:700}
.post-date{left:717px;top:614px;font-size:8px;color:#4a4656}
.post-bubble{left:552px;top:630px;width:232px;height:39px;background:var(--post);border:1px solid var(--post-line);border-radius:5px;padding:8px 17px;font-size:7px;line-height:10px;color:#3b3550}
.post-avatar{left:797px;top:634px;width:32px;height:32px;border-radius:50%;background:linear-gradient(160deg,#d9b36a,#6b4e36);border:2px solid #dcdce4}
.chat{width:18px;height:18px;border-radius:50%}
.chat i{position:absolute;top:8px;width:2px;height:2px;border-radius:50%;background:var(--white)}
.copyright{right:36px;top:760px;font-size:8px;color:#4a4656}
.copyright b{color:var(--blue)}
.popup{left:625px;top:428px;width:220px;height:283px;background:var(--popup);border:2px solid var(--popup-line);border-radius:12px;box-shadow:0 3px 8px rgba(0,0,0,.15)}
.popup-mail{position:absolute;left:22px;top:16px;width:36px;height:34px;border-radius:6px;background:var(--white)}
.popup-mail i{position:absolute;left:11px;top:11px;width:14px;height:12px;border-radius:2px;background:var(--ink)}
.popup-title{position:absolute;left:70px;top:27px;font-size:11px;font-weight:700;color:var(--cyan)}
.popup-close{position:absolute;left:195px;top:9px;width:13px;height:13px;border-radius:3px;background:var(--red)}
.field{position:absolute;left:23px;width:177px;height:25px;border-radius:4px;background:#d5ecfc;font-size:8px;color:#6d6a78;padding:6px 8px}
.send{position:absolute;left:23px;top:238px;width:177px;height:26px;border-radius:4px;background:var(--green);color:var(--white);font-size:10px;font-weight:700;text-align:center;line-height:27px}
</style>
</head>
<body>

<!-- Dashboard view -->
<div class="screen screen-a">
  <div class="abs header" role="img" aria-label="Header photo of hands typing on a laptop, tinted purple"></div>
  <div class="abs sidebar"></div>
  <div class="abs sidebar-head"></div>
  <div class="abs footer"></div>
  <div class="abs avatar" role="img" aria-label="Student profile photo"></div>
  <div class="abs welcome">Welcome</div>
  <div class="abs user-name">Lucas Brandt</div>
  <div class="abs brand">Learnway</div>
  <div class="abs crumbs">Dashboard &nbsp;›&nbsp; Projects &nbsp;›&nbsp; Profile paper Havo 2020-2021 &nbsp;›&nbsp; <b>Example</b></div>
  <div class="abs top-dot" style="left:812px"><i></i></div>
  <div class="abs top-dot" style="left:839px"></div>

  <div class="abs tab active" style="left:250px">Progress</div>
  <div class="abs tab" style="left:334px">Tools</div>
  <div class="abs tab" style="left:392px">Messages</div>
  <div class="abs tool-icon" style="left:784px"></div>
  <div class="abs tool-icon" style="left:814px;background:#8d8a98"></div>
  <div class="abs tool-icon" style="left:843px"></div>

  <div class="abs nav-icon" style="top:149px;background:var(--ink)"></div><div class="abs nav strong" style="top:144px">Dashboard</div><div class="abs burger"></div>
  <div class="abs nav-icon" style="top:191px"></div><div class="abs nav current" style="top:186px">Projects</div>
  <div class="abs nav-icon" style="top:233px"></div><div class="abs nav" style="top:228px">Online</div>
  <div class="abs nav-icon" style="top:275px;background:#9d99a8"></div><div class="abs nav" style="top:270px">Profile</div>
  <div class="abs nav-icon" style="top:317px"></div><div class="abs nav" style="top:312px">App</div>
  <div class="abs nav-icon" style="top:359px"></div><div class="abs nav" style="top:354px">Opportunities</div>
  <div class="abs nav-icon" style="top:401px;background:#9d99a8"></div><div class="abs nav" style="top:396px">Help</div>
  <div class="abs nav-icon" style="top:470px;background:#9d99a8"></div><div class="abs nav" style="top:465px;color:#4a4656;font-weight:600">Tools</div>

  <div class="abs section-title" style="left:249px;top:163px">Timeline</div>
  <div class="abs arrow-btn prev"></div>
  <div class="abs arrow-btn next"></div>
  <div class="abs timeline"></div>
  <div class="abs track"></div>
  <div class="abs step done" style="left:269px">01<span class="badge" style="background:var(--green)"><svg width="14" height="14"><path d="M4 7l2 2 4-4" stroke="#fff" stroke-width="1.6" fill="none"/></svg></span></div>
  <div class="abs step done" style="left:372px">02<span class="badge" style="background:var(--green)"><svg width="14" height="14"><path d="M4 7l2 2 4-4" stroke="#fff" stroke-width="1.6" fill="none"/></svg></span></div>
  <div class="abs step done" style="left:475px">03<span class="badge" style="background:var(--green)"><svg width="14" height="14"><path d="M4 7l2 2 4-4" stroke="#fff" stroke-width="1.6" fill="none"/></svg></span></div>
  <div class="abs step edit" style="left:579px">04<span class="badge" style="background:var(--blue)"><svg width="14" height="14"><path d="M4 10l6-6" stroke="#fff" stroke-width="1.6"/></svg></span></div>
  <div class="abs step wait" style="left:682px">05<span class="badge" style="background:var(--yellow-dot)"><svg width="14" height="14"><path d="M4 7h1M7 7h1M10 7h1" stroke="#fff" stroke-width="1.6"/></svg></span></div>
  <div class="abs step stop" style="left:785px">06<span class="badge" style="background:var(--red)"><svg width="14" height="14"><path d="M5 5l4 4M9 5l-4 4" stroke="#fff" stroke-width="1.6"/></svg></span></div>
  <div class="abs step-date" style="left:256px">00 Month</div>
  <div class="abs step-date" style="left:359px">00 Month</div>
  <div class="abs step-date" style="left:462px">00 Month</div>
  <div class="abs step-date" style="left:566px">00 Month</div>
  <div class="abs step-date" style="left:669px">00 Month</div>
  <div class="abs step-date" style="left:772px">00 Month</div>

  <div class="abs section-title" style="left:250px;top:305px">Documents</div>
  <div class="abs doc" style="top:338px"><span class="doc-icon light" style="left:18px"></span><span class="doc-label">Paper</span><span class="doc-icon light" style="left:174px"></span><span class="doc-icon light" style="left:206px"></span><span class="doc-icon" style="left:236px"></span></div>
  <div class="abs doc featured" style="top:409px"><span class="doc-icon" style="left:18px;border-radius:50%"></span><span class="doc-label">Plan of action</span><span class="doc-icon" style="left:174px;border-radius:50%"></span><span class="doc-icon light" style="left:204px"></span><span class="doc-icon" style="left:236px"></span></div>
  <div class="abs doc" style="top:480px"><span class="doc-icon" style="left:18px"></span><span class="doc-label">Powerpoint</span><span class="doc-icon light" style="left:204px"></span><span class="doc-icon" style="left:236px"></span></div>

  <div class="abs section-title" style="left:552px;top:305px">Upcomming appointments</div>
  <div class="abs view-all" style="left:807px;top:309px">View all ›</div>
  <div class="abs appt" style="top:338px"><span class="appt-title">Submittng reseach proposal</span><span class="appt-date">00 Month</span><span class="appt-flag" style="background:var(--green)"></span></div>
  <div class="abs pill">Planning</div>
  <div class="abs appt" style="top:409px"><span class="appt-title">Example</span><span class="appt-date">00 Month</span><span class="appt-flag" style="background:var(--yellow-dot)"></span></div>
  <div class="abs appt" style="top:480px"><span class="appt-title">Evaluation</span><span class="appt-date">00 Month</span><span class="appt-flag" style="background:var(--red)"></span></div>

  <div class="abs section-title" style="left:551px;top:573px">Recent posts</div>
  <div class="abs view-all" style="left:807px;top:577px">View all ›</div>
  <div class="abs post-author">Tom Hendriks</div>
  <div class="abs post-date">4-02-2021 at 19:39</div>
  <div class="abs post-bubble">Lorem ipsum dolor sit amet, consectetur adipiscing elit donec consectetur semper nunc in molestie.</div>
  <div class="abs post-avatar" role="img" aria-label="Author profile photo"></div>
  <div class="abs chat" style="left:837px;top:676px;background:#8d8a98"><i style="left:4px"></i><i style="left:8px"></i><i style="left:12px"></i></div>

  <div class="abs copyright">Copytight &nbsp;2020 <b>Learnway</b> All rights reserved</div>
</div>

<!-- Dashboard view with message form open -->
<div class="screen screen-b">
  <div class="abs header" role="img" aria-label="Header photo of hands typing on a laptop, tinted purple"></div>
  <div class="abs sidebar"></div>
  <div class="abs sidebar-head"></div>
  <div class="abs footer"></div>
  <div class="abs avatar" role="img" aria-label="Student profile photo"></div>
  <div class="abs welcome">Welcome</div>
  <div class="abs user-name">Lucas Brandt</div>
  <div class="abs brand">Learnway</div>
  <div class="abs crumbs">Dashboard &nbsp;›&nbsp; Projects &nbsp;›&nbsp; Profile paper Havo 2020-2021 &nbsp;›&nbsp; <b>Example</b></div>
  <div class="abs top-dot" style="left:812px"><i></i></div>
  <div class="abs top-dot" style="left:839px"></div>

  <div class="abs tab active" style="left:250px">Progress</div>
  <div class="abs tab" style="left:334px">Tools</div>
  <div class="abs tab" style="left:392px">Messages</div>
  <div class="abs tool-icon" style="left:784px"></div>
  <div class="abs tool-icon" style="left:814px;background:#8d8a98"></div>
  <div class="abs tool-icon" style="left:843px"></div>

  <div class="abs nav-icon" style="top:149px;background:var(--ink)"></div><div class="abs nav strong" style="top:144px">Dashboard</div><div class="abs burger"></div>
  <div class="abs nav-icon" style="top:191px"></div><div class="abs nav current" style="top:186px">Projects</div>
  <div class="abs nav-icon" style="top:233px"></div><div class="abs nav" style="top:228px">Online</div>
  <div class="abs nav-icon" style="top:275px;background:#9d99a8"></div><div class="abs nav" style="top:270px">Profile</div>
  <div class="abs nav-icon" style="top:317px"></div><div class="abs nav" style="top:312px">App</div>
  <div class="abs nav-icon" style="top:359px"></div><div class="abs nav" style="top:354px">Opportunities</div>
  <div class="abs nav-icon" style="top:401px;background:#9d99a8"></div><div class="abs nav" style="top:396px">Help</div>
  <div class="abs nav-icon" style="top:470px;background:#9d99a8"></div><div class="abs nav" style="top:465px;color:#4a4656;font-weight:600">Tools</div>

  <div class="abs section-title" style="left:249px;top:163px">Timeline</div>
  <div class="abs arrow-btn prev"></div>
  <div class="abs arrow-btn next"></div>
  <div class="abs timeline"></div>
  <div class="abs track"></div>
  <div class="abs step done" style="left:269px">01<span class="badge" style="background:var(--green)"><svg width="14" height="14"><path d="M4 7l2 2 4-4" stroke="#fff" stroke-width="1.6" fill="none"/></svg></span></div>
  <div class="abs step done" style="left:372px">02<span class="badge" style="background:var(--green)"><svg width="14" height="14"><path d="M4 7l2 2 4-4" stroke="#fff" stroke-width="1.6" fill="none"/></svg></span></div>
  <div class="abs step done" style="left:475px">03<span class="badge" style="background:var(--green)"><svg width="14" height="14"><path d="M4 7l2 2 4-4" stroke="#fff" stroke-width="1.6" fill="none"/></svg></span></div>
  <div class="abs step edit" style="left:579px">04<span class="badge" style="background:var(--blue)"><svg width="14" height="14"><path d="M4 10l6-6" stroke="#fff" stroke-width="1.6"/></svg></span></div>
  <div class="abs step wait" style="left:682px">05<span class="badge" style="background:var(--yellow-dot)"><svg width="14" height="14"><path d="M4 7h1M7 7h1M10 7h1" stroke="#fff" stroke-width="1.6"/></svg></span></div>
  <div class="abs step stop" style="left:785px">06<span class="badge" style="background:var(--red)"><svg width="14" height="14"><path d="M5 5l4 4M9 5l-4 4" stroke="#fff" stroke-width="1.6"/></svg></span></div>
  <div class="abs step-date" style="left:256px">00 Month</div>
  <div class="abs step-date" style="left:359px">00 Month</div>
  <div class="abs step-date" style="left:462px">00 Month</div>
  <div class="abs step-date" style="left:566px">00 Month</div>
  <div class="abs step-date" style="left:669px">00 Month</div>
  <div class="abs step-date" style="left:772px">00 Month</div>

  <div class="abs section-title" style="left:250px;top:305px">Documents</div>
  <div class="abs doc" style="top:338px"><span class="doc-icon light" style="left:18px"></span><span class="doc-label">Paper</span><span class="doc-icon light" style="left:174px"></span><span class="doc-icon light" style="left:206px"></span><span class="doc-icon" style="left:236px"></span></div>
  <div class="abs doc featured" style="top:409px"><span class="doc-icon" style="left:18px;border-radius:50%"></span><span class="doc-label">Plan of action</span><span class="doc-icon" style="left:174px;border-radius:50%"></span><span class="doc-icon light" style="left:204px"></span><span class="doc-icon" style="left:236px"></span></div>
  <div class="abs doc" style="top:480px"><span class="doc-icon" style="left:18px"></span><span class="doc-label">Powerpoint</span><span class="doc-icon light" style="left:204px"></span><span class="doc-icon" style="left:236px"></span></div>

  <div class="abs section-title" style="left:552px;top:305px">Upcomming appointments</div>
  <div class="abs view-all" style="left:807px;top:309px">View all ›</div>
  <div class="abs appt" style="top:338px"><span class="appt-title">Submittng reseach proposal</span><span class="appt-date">00 Month</span><span class="appt-flag" style="background:var(--green)"></span></div>
  <div class="abs pill">Planning</div>
  <div class="abs appt" style="top:409px"><span class="appt-title">Example</span><span class="appt-date">00 Month</span><span class="appt-flag" style="background:var(--yellow-dot)"></span></div>
  <div class="abs appt" style="top:480px"><span class="appt-title">Evaluation</span><span class="appt-date">00 Month</span><span class="appt-flag" style="background:var(--red)"></span></div>

  <div class="abs section-title" style="left:551px;top:573px">Recent posts</div>
  <div class="abs view-all" style="left:848px;top:577px">›</div>
  <div class="abs post-author">Tom Hendriks</div>
  <div class="abs post-bubble">Lorem ipsum dolor sit amet, consectetur adipiscing elit donec consectetur semper nunc in molestie.</div>

  <div class="abs popup">
    <span class="popup-mail"><i></i></span>
    <span class="popup-title">Leave a message</span>
    <span class="popup-close"></span>
    <span class="field" style="top:77px">Your name (Required)</span>
    <span class="field" style="top:113px">Your email (Required)</span>
    <span class="field" style="top:152px;height:70px">Your message</span>
    <span class="send">Send ➤</span>
  </div>
  <div class="abs chat" style="left:855px;top:695px;background:var(--ink)"><i style="left:4px"></i><i style="left:8px"></i><i style="left:12px"></i></div>

  <div class="abs copyright">Copytight &nbsp;2020 <b>Learnway</b> All rights reserved</div>
</div>

</body>
</html>
```